Plakat für Schaufenster
Zielgruppe
Moin Moin,
ich habe einen kleinen Fahrradladen in einem historischen Gebäude. Wir führen ein sehr hochwertiges und ausgesuchtes Programm diverser Hersteller und bieten eine umfassende individuelle Beratung
Aufgabenstellung
Ein Fahrradladen ist einerseits ein Handwerksbetrieb anderseits auch ein Handelsbetrieb. Da ich als Einzelkämpfer in meinem Laden arbeite, habe ich diese beiden Betriebe zeitlich voneinander getrennt. Ich arbeite Vormittags in der Werkstatt und Nachmitttags ist mein Laden für Service und Beratung geöffnet, d.h. meine Laden ist nur Nachmittags von 14-18 und Samstag von 10-13 Uhr geöffnet. Durch diese Regelung kann ich kurze Reparaturzeiten und gute Beratung bieten.
Leider denken nun viele Menschen wenn Sie Vormittags vor verschlossener Tür stehen: "der hat es nicht nötig und arbeitet nur noch halbe Tage!".
Nun möchte ich mit einem Plakat im Fenster meinen "geteilten" Betrieb bzw. meine Arbeitsteilung erklären.
Vielleicht in Form einer analogen Uhr mit entsprechender Teilung !?! Aber auch andere Ideen sind herzlich Willkommen !!

```html
<!DOCTYPE html>
<html lang="de">
<head>
<meta charset="utf-8">
<title>Werkstatt · Service &amp; Beratung – Schaufensterplakat</title>
<link href="https://fonts.googleapis.com/css2?family=Fjalla+One&display=swap" rel="stylesheet">
<style>
  :root {
    --backdrop: #ffffff;
    --paper: #f0c997;
    --band-orange: #ef7b22;
    --accent-orange: #e8712a;
    --ink: #0d0d0d;
    --pale-peach: #f3cd9f;
  }
  html, body {
    margin: 0;
    padding: 0;
    width: 1200px;
    height: 1200px;
    overflow: hidden;
    background: var(--backdrop);
  }
  .canvas {
    position: relative;
    width: 1200px;
    height: 1200px;
  }
  .poster {
    position: absolute;
    left: 190px;
    top: 20px;
    width: 821px;
    height: 1160px;
    display: block;
  }
  .poster-paper { fill: var(--paper); }
  .poster-band { fill: var(--band-orange); }
  .poster-frame { fill: none; stroke: var(--ink); stroke-width: 1.5; }
  .poster-text {
    font-family: "Fjalla One", "Oswald", sans-serif;
    text-anchor: middle;
  }
  .headline { fill: var(--ink); }
  .headline--workshop { font-size: 92px; }
  .headline--service { font-size: 94px; }
  .schedule--morning { fill: var(--accent-orange); font-size: 40px; }
  .schedule--afternoon { fill: var(--pale-peach); font-size: 40px; }
  .bicycle-illustration { fill: url(#bicycleTone); }
</style>
</head>
<body>
<main class="canvas">
  <svg class="poster" viewBox="0 0 821 1160" xmlns="http://www.w3.org/2000/svg">
    <defs>
      <radialGradient id="bicycleTone" cx="50%" cy="55%" r="60%">
        <stop offset="0%" stop-color="#1a1a1a" stop-opacity="0.35"/>
        <stop offset="100%" stop-color="#1a1a1a" stop-opacity="0.12"/>
      </radialGradient>
    </defs>

    <rect class="poster-paper" x="0" y="0" width="821" height="1160"/>
    <rect class="poster-band" x="0" y="580" width="821" height="580"/>
    <rect class="poster-frame" x="22" y="22" width="777" height="1117"/>

    <text class="poster-text headline headline--workshop" x="414" y="183"
          textLength="352" lengthAdjust="spacingAndGlyphs">Werkstatt</text>
    <text class="poster-text schedule--morning" x="414" y="264"
          textLength="264" lengthAdjust="spacingAndGlyphs">Montag – Freitag</text>
    <text class="poster-text schedule--morning" x="414" y="319"
          textLength="155" lengthAdjust="spacingAndGlyphs">Vormittag</text>

    <rect class="bicycle-illustration" x="65" y="380" width="694" height="398" rx="8"
          role="img" aria-label="Illustration eines klassischen Herrenfahrrads im Stil eines alten Kupferstichs"/>

    <text class="poster-text headline headline--service" x="414" y="913"
          textLength="677" lengthAdjust="spacingAndGlyphs">Service &amp; Beratung</text>
    <text class="poster-text schedule--afternoon" x="414" y="995"
          textLength="563" lengthAdjust="spacingAndGlyphs">Montag – Freitag 14:00 – 18:00 Uhr</text>
    <text class="poster-text schedule--afternoon" x="414" y="1049"
          textLength="431" lengthAdjust="spacingAndGlyphs">Samstag 10:00 – 13:00 Uhr</text>
  </svg>
</main>
</body>
</html>
```